Home Staging Company needs business card design

We're a home staging company called Brightwell Harbor Home Staging. We would like a business card design that includes aqua and gray. Our current logo of house within chair is fine but I find we almost always use the logo in one color. I'll upload images of front and back of our current card and our logo. Note that we have dropped "Solutions" from our company name and don't want to include it on the card.

Target Market(s)

Realtors and homeowners - people interested in selling their homes

Contact Information for Business Card

Marisol Fenwickley
Brightwell Harbor Home Staging
757-382-6190
www.brightwellharbor.com
marisol@brightwellharbor.com

Font styles to use
Serif
Script

Requirements
Must have
• My logo and contact details
• UPDATE***
• I forgot to say that the company name should be included on the front of the card somehow.

```html
<!DOCTYPE html>
<html lang="en">
<head>
<meta charset="utf-8">
<title>Brightwell Harbor Home Staging – Business Card</title>
<link rel="stylesheet" href="https://fonts.googleapis.com/css2?family=Playfair+Display:wght@400&family=Open+Sans:wght@400;600&display=swap">
<style>
  :root {
    --backdrop: #1b1c1f;
    --card-dark: #1f2023;
    --card-mid: #2e3034;
    --brand-blue: #4a86d4;
    --aqua: #5eaede;
    --text-light: #f4f5f7;
  }
  html, body {
    margin: 0;
    width: 1200px;
    height: 1101px;
    overflow: hidden;
    background: var(--backdrop);
  }
  .canvas {
    position: relative;
    width: 1200px;
    height: 1101px;
  }
  .card {
    position: absolute;
    left: 190px;
    width: 820px;
    height: 469px;
    overflow: hidden;
    border-radius: 4px;
    background: radial-gradient(ellipse at 55% 40%, var(--card-mid) 0%, var(--card-dark) 70%);
    box-shadow: 0 18px 40px rgba(0,0,0,.55);
  }
  .card--back { top: 51px; }
  .card--front { top: 581px; }

  .halftone {
    position: absolute;
    top: 0;
    bottom: 0;
  }
  .card--back .halftone {
    left: 0;
    width: 520px;
    background: linear-gradient(90deg, rgba(74,134,212,.75) 0%, rgba(74,134,212,.35) 45%, rgba(74,134,212,0) 100%);
  }
  .card--front .halftone {
    right: 0;
    width: 440px;
    background: linear-gradient(270deg, rgba(94,174,222,.7) 0%, rgba(94,174,222,.3) 50%, rgba(94,174,222,0) 100%);
  }

  .brand {
    position: absolute;
    display: flex;
    align-items: center;
    gap: 18px;
  }
  .brand__mark {
    flex: none;
    border-radius: 50%;
    background: var(--text-light);
  }
  .brand__name {
    font-family: "Playfair Display", serif;
    font-weight: 400;
    color: var(--brand-blue);
    line-height: 1.1;
  }
  .card--back .brand { left: 400px; top: 300px; }
  .card--back .brand__mark { width: 62px; height: 62px; }
  .card--back .brand__name { font-size: 30px; }

  .card--front .brand { left: 62px; top: 58px; }
  .card--front .brand__mark { width: 96px; height: 96px; }
  .card--front .brand__name { font-size: 40px; }

  .person {
    position: absolute;
    left: 72px;
    top: 235px;
    margin: 0;
    font-family: "Open Sans", sans-serif;
    font-weight: 600;
    font-size: 28px;
    color: var(--brand-blue);
  }
  .contacts {
    position: absolute;
    left: 64px;
    top: 298px;
    margin: 0;
    padding: 0;
    list-style: none;
    font-family: "Open Sans", sans-serif;
    font-size: 20px;
    color: var(--text-light);
  }
  .contacts__item {
    display: flex;
    align-items: center;
    gap: 12px;
    height: 44px;
  }
  .contacts__icon {
    width: 24px;
    height: 24px;
    fill: none;
    stroke: var(--brand-blue);
    stroke-width: 2;
    stroke-linecap: round;
    stroke-linejoin: round;
  }
</style>
</head>
<body>
<main class="canvas">

  <section class="card card--back" aria-label="Card back">
    <div class="halftone" role="img" aria-label="Blue halftone dot pattern fading from the left edge"></div>
    <div class="brand">
      <span class="brand__mark"></span>
      <span class="brand__name">Brightwell Harbor<br>Home Staging</span>
    </div>
  </section>

  <section class="card card--front" aria-label="Card front">
    <div class="halftone" role="img" aria-label="Aqua halftone dot pattern fading from the right edge"></div>
    <div class="brand">
      <span class="brand__mark"></span>
      <span class="brand__name">Brightwell Harbor<br>Home Staging</span>
    </div>

    <p class="person">Marisol Fenwickley</p>

    <ul class="contacts">
      <li class="contacts__item">
        <svg class="contacts__icon" viewBox="0 0 24 24" aria-hidden="true">
          <path d="M5 3h4l2 5-2.5 1.5a11 11 0 0 0 6 6L16 13l5 2v4a2 2 0 0 1-2 2A16 16 0 0 1 3 5a2 2 0 0 1 2-2z"/>
        </svg>
        <span>757-382-6190</span>
      </li>
      <li class="contacts__item">
        <svg class="contacts__icon" viewBox="0 0 24 24" aria-hidden="true">
          <circle cx="12" cy="12" r="9"/>
          <path d="M3 12h18M12 3a14 14 0 0 1 0 18M12 3a14 14 0 0 0 0 18"/>
        </svg>
        <span>www.brightwellharbor.com</span>
      </li>
      <li class="contacts__item">
        <svg class="contacts__icon" viewBox="0 0 24 24" aria-hidden="true">
          <rect x="3" y="5" width="18" height="14" rx="2"/>
          <path d="M3 7l9 6 9-6"/>
        </svg>
        <span>marisol@brightwellharbor.com</span>
      </li>
    </ul>
  </section>

</main>
</body>
</html>
```